Cans for flavored Macadamias

Brindle Creek Orchard Company (www.brindlecreekorchard.example) has been packaging 3 flavors of macadamia nuts in to 200g pouches for a number of years. We are about to change from 200g pouches to 80g cans. We need a fresh new look although the back ground colours must stay the same, Roasted & Salted = Yellow, Wasabi = Green, Abalone = Blue.
The can label and lid sticker will be printed 4 colour process. The trimmed finished sizes are, can label - L246 x H60mm and lid sticker 61mm diameter. The attached files show the existing front and back labels for the pouches. The health benefits, ingredients and nutrition facts information can used. Delete address and bar code but leave space for new ones. '80g Net' must show on the front of the can label. Product of Australia logo must be prominent on both can label and lid sticker.
The general feeling is we need to have a photo of a koala on there somewhere, maybe the lid. I have uploaded a photo that I hope you can use.
Updates

Target Market(s)

We're in all of Australia's duty free stores and a lot of souvenir stores. We do sell in to retails. Our target customers are primarily Asian hence the Wasabi and Abalone flavours.

Industry/Entity Type

It Company

Requirements
Must have
• If you google images for "buy Australian flavoured macadamias" it shows most of what's currently on the market. We obviously don't want to look the same as any of them.

```html
<!DOCTYPE html>
<html lang="en">
<head>
<meta charset="utf-8">
<title>Brindle Creek Macadamia Nuts – Can Labels</title>
<link rel="stylesheet" href="https://fonts.googleapis.com/css2?family=Amatic+SC:wght@400;700&display=swap">
<style>
  :root {
    --backdrop-top: #d9d9d9;
    --backdrop-bottom: #ffffff;
    --sun-yellow: #f4e41c;
    --ink-brown: #6b3a12;
    --title-white: #ffffff;
    --ribbon-brown: #7a3f16;
    --tag-yellow: #f6e52a;
    --wasabi-mid: #7cb63a;
    --wasabi-deep: #2e7a2a;
    --abalone-mid: #3d8fd6;
    --abalone-deep: #1c5aa3;
    --salted-mid: #e0a22c;
    --salted-deep: #94561c;
    --sign-wasabi: #8dbf3c;
    --sign-abalone: #3a3f9c;
    --sign-salted: #f0c92a;
  }
  * { box-sizing: border-box; margin: 0; padding: 0; }
  html, body { width: 1200px; height: 1000px; overflow: hidden; }
  body {
    background: linear-gradient(180deg, var(--backdrop-top) 0%, var(--backdrop-bottom) 55%);
    font-family: "Amatic SC", cursive;
    position: relative;
  }
  .label {
    position: absolute;
    width: 340px;
    height: 420px;
    overflow: hidden;
    border-radius: 4px;
    box-shadow: 0 6px 18px rgba(0,0,0,0.18);
  }
  .label--wasabi {
    left: 50px; top: 290px;
    background: linear-gradient(180deg, var(--sun-yellow) 0%, var(--sun-yellow) 22%, var(--wasabi-mid) 55%, var(--wasabi-deep) 100%);
  }
  .label--abalone {
    left: 430px; top: 230px;
    transform: scale(1.15); transform-origin: top left;
    background: linear-gradient(180deg, var(--sun-yellow) 0%, var(--sun-yellow) 16%, var(--abalone-mid) 30%, var(--abalone-deep) 100%);
  }
  .label--salted {
    left: 810px; top: 290px;
    background: linear-gradient(180deg, var(--sun-yellow) 0%, var(--sun-yellow) 40%, var(--salted-mid) 65%, var(--salted-deep) 100%);
  }
  .tagline {
    position: absolute; top: 14px; left: 0; right: 0;
    text-align: center; font-size: 24px; font-weight: 700;
    color: var(--ink-brown); letter-spacing: 1px;
  }
  .horizon {
    position: absolute; top: 48px; left: 0; right: 0; height: 50px;
  }
  .label--wasabi .horizon { background: linear-gradient(180deg, rgba(244,228,28,0) 0%, #8fbf3a 60%, #6ea62e 100%); }
  .label--abalone .horizon { background: linear-gradient(180deg, rgba(244,228,28,0) 0%, #4c9ad8 60%, #3d8fd6 100%); }
  .label--salted .horizon { background: linear-gradient(180deg, rgba(244,228,28,0) 0%, #e8b832 60%, #e0a22c 100%); }
  .title {
    position: absolute; top: 92px; left: 0; right: 0;
    text-align: center; color: var(--title-white);
    font-weight: 700; line-height: 0.9;
    text-shadow: 2px 3px 0 rgba(0,0,0,0.18);
  }
  .title__line { display: block; font-size: 88px; }
  .brand-badge {
    position: absolute; left: 18px; top: 262px; width: 110px; height: 110px;
  }
  .brand-badge__photo {
    width: 96px; height: 96px; margin-left: 7px;
    border-radius: 50%;
    border: 6px solid var(--tag-yellow);
    background: radial-gradient(circle at 45% 40%, #c9c4bd 0%, #8d8782 60%, #5e5a56 100%);
  }
  .brand-badge__name {
    position: absolute; left: -6px; top: 74px; width: 122px;
    background: var(--ribbon-brown); color: var(--tag-yellow);
    font-size: 20px; font-weight: 700; text-align: center;
    padding: 1px 0;
  }
  .tasting-tag {
    position: absolute; right: 16px; top: 246px;
    background: var(--tag-yellow); color: var(--ink-brown);
    font-size: 20px; font-weight: 700; padding: 0 10px;
  }
  .flavour-sign {
    position: absolute; right: 26px; top: 288px; width: 104px;
    border: 2px solid var(--tag-yellow);
    padding: 6px 4px; text-align: center; line-height: 0.95;
  }
  .label--wasabi .flavour-sign { background: var(--sign-wasabi); color: var(--tag-yellow); }
  .label--abalone .flavour-sign { background: var(--sign-abalone); color: var(--tag-yellow); }
  .label--salted .flavour-sign { background: var(--sign-salted); color: var(--ink-brown); }
  .flavour-sign__name { display: block; font-size: 30px; font-weight: 700; }
  .flavour-sign__note { display: block; font-size: 18px; font-weight: 700; }
  .net-weight {
    position: absolute; left: 140px; top: 338px;
    color: var(--tag-yellow); font-size: 22px; font-weight: 700;
  }
</style>
</head>
<body>

<section class="label label--wasabi">
  <p class="tagline">Lightly Roasted</p>
  <div class="horizon" role="img" aria-label="Outback hills with kangaroo silhouettes and a rising sun"></div>
  <h2 class="title"><span class="title__line">Macadamia</span><span class="title__line">Nuts</span></h2>
  <div class="brand-badge">
    <div class="brand-badge__photo" role="img" aria-label="Photo of koalas"></div>
    <p class="brand-badge__name">Brindle Creek</p>
  </div>
  <p class="tasting-tag">Great Tasting</p>
  <div class="flavour-sign"><span class="flavour-sign__name">Wasabi</span><span class="flavour-sign__note">Flavoured</span></div>
  <p class="net-weight">Net Wt. 80g</p>
</section>

<section class="label label--abalone">
  <p class="tagline">Lightly Roasted</p>
  <div class="horizon" role="img" aria-label="Outback hills with kangaroo silhouettes and a rising sun"></div>
  <h2 class="title"><span class="title__line">Macadamia</span><span class="title__line">Nuts</span></h2>
  <div class="brand-badge">
    <div class="brand-badge__photo" role="img" aria-label="Photo of koalas"></div>
    <p class="brand-badge__name">Brindle Creek</p>
  </div>
  <p class="tasting-tag">Great Tasting</p>
  <div class="flavour-sign"><span class="flavour-sign__name">Abalone</span><span class="flavour-sign__note">Flavoured</span></div>
  <p class="net-weight">Net Wt. 80g</p>
</section>

<section class="label label--salted">
  <p class="tagline">Australia's Finest</p>
  <div class="horizon" role="img" aria-label="Outback hills with kangaroo silhouettes and a rising sun"></div>
  <h2 class="title"><span class="title__line">Macadamia</span><span class="title__line">Nuts</span></h2>
  <div class="brand-badge">
    <div class="brand-badge__photo" role="img" aria-label="Photo of koalas"></div>
    <p class="brand-badge__name">Brindle Creek</p>
  </div>
  <p class="tasting-tag">Great Tasting</p>
  <div class="flavour-sign"><span class="flavour-sign__name">Roasted</span><span class="flavour-sign__note">and Salted</span></div>
  <p class="net-weight">Net Wt. 80g</p>
</section>

</body>
</html>
```